Buchcover spirituelles Projekt 12 x 19 cm
Zielgruppe
Meine Zielgruppe sind Menschen die an Grundwissen über Spiritualität und die Kraft der Gedanken interessiert sind und den Glauben besitzen mit der Kraft Ihrer Gedanken Ihr Leben zu verändern.
Aufgabenstellung
Ich suche ein Cover in 12 x 19 cm für ein Grundlagenwerk über Affirmationen. Inhalt des Buches sind Anleitungen mit dem Umgang von Affirmationen in Bezug auf Energie-Zentren und Lebensthemen.
Titel:
QUELLKRAFT DER LEITSÄTZE
Gesundheit für Körper und Seele
von Renate Kolbeck & Matthias Grauwald
Auf der Vorderseite sollte noch ein Hinweis sein: inklusive Gratis-Download der Meditation "Der Fluss der Klärung, Stärkung und Erneuerung"
Auf der Rückseite soll ein kleiner Text sein und unser Foto (Siehe Anhang), Platz für den Strichcode
Aktuell interessiert uns nur das Design. Wenn der Satz fertig ist in ca vier Wochen, müsste dann genau nachgearbeitet werden. Dann können wir auch genaue Angaben machen wegen Buchrückendicke, ISBN -Nummer etc. mitteilen. Diese Arbeit sollte im Preis enthalten sein und nicht zusätzlich nachhonoriert werden.
Wir benötigen dann 3 verschiedene Versionen des Umschlags für:
HardCover
SoftCover
eBook
Wir haben keine Präferenzen bezüglich der Gestaltung, nur bitte nicht düster oder gruselig.
Nachsatz_
Wir möchten, unser Foto auch auf der Vorderseite zu sehen ist, sprich freigestellt und auf möglichst einfarbigen Hintergrund zu sehen ist. Hier sind wir aber offen.

```html
<!DOCTYPE html>
<html lang="de">
<head>
<meta charset="utf-8">
<title>Quellkraft der Leitsätze – Buchcover</title>
<link rel="stylesheet" href="https://fonts.googleapis.com/css2?family=Libre+Baskerville&family=Signika:wght@400&family=Oswald:wght@500&display=swap">
<style>
  :root {
    --stage: #2a2a2c;
    --title-red: #8e1a48;
    --title-blue: #1d4a8a;
    --ink: #2b1f2a;
    --author: #b0226a;
    --glow: #fffbe8;
    --pink: #ef6fa6;
    --lilac: #e9c8e4;
    --sky: #7fa6da;
    --sea: #3f9fc7;
    --badge: #a7398f;
    --badge-dark: #7a2468;
  }
  html, body {
    margin: 0;
    width: 1200px;
    height: 896px;
    overflow: hidden;
    background: var(--stage);
  }
  .cover {
    position: absolute;
    left: 335px;
    top: 28px;
    width: 530px;
    height: 840px;
    overflow: hidden;
    background:
      radial-gradient(ellipse 150px 130px at 268px 470px, var(--glow) 0%, rgba(255,245,200,0.7) 40%, rgba(255,255,255,0) 100%),
      radial-gradient(ellipse 230px 160px at 100px 560px, rgba(239,111,166,0.75), rgba(239,111,166,0) 100%),
      radial-gradient(ellipse 210px 150px at 440px 330px, rgba(239,111,166,0.6), rgba(239,111,166,0) 100%),
      linear-gradient(180deg, #f7f3f8 0%, #f4eaf2 22%, var(--lilac) 38%, #f3b5d1 55%, #e9a0c8 66%, var(--sky) 82%, var(--sea) 100%);
  }
  .hands-photo {
    position: absolute;
    left: 131px;
    top: 457px;
    width: 270px;
    height: 383px;
    background: radial-gradient(ellipse at 50% 35%, rgba(255,250,240,0.9) 0%, rgba(228,196,184,0.75) 45%, rgba(200,170,170,0.35) 80%, rgba(200,170,170,0) 100%);
  }
  .title {
    position: absolute;
    left: 0;
    width: 100%;
    top: 58px;
    margin: 0;
    text-align: center;
    font-family: "Libre Baskerville", serif;
    font-weight: 400;
    font-size: 50px;
    line-height: 62px;
    letter-spacing: -0.5px;
  }
  .title-line-one { display: block; color: var(--title-red); }
  .title-line-two { display: block; color: var(--title-blue); }
  .subtitle {
    position: absolute;
    left: 0;
    width: 100%;
    top: 208px;
    margin: 0;
    text-align: center;
    font-family: "Libre Baskerville", serif;
    font-size: 21px;
    color: var(--ink);
  }
  .ornament {
    position: absolute;
    left: 144px;
    top: 274px;
    width: 256px;
    height: 36px;
    border-radius: 18px;
    background: linear-gradient(90deg, rgba(90,40,70,0) 0%, rgba(90,40,70,0.25) 50%, rgba(90,40,70,0) 100%);
  }
  .authors {
    position: absolute;
    left: 0;
    width: 100%;
    top: 345px;
    margin: 0;
    text-align: center;
    font-family: "Signika", sans-serif;
    font-size: 15px;
    color: var(--author);
  }
  .badge {
    position: absolute;
    left: 385px;
    top: 690px;
    width: 124px;
    height: 124px;
  }
  .badge text { font-family: "Oswald", sans-serif; font-weight: 500; }
</style>
</head>
<body>
  <main class="cover">
    <div class="hands-photo" role="img" aria-label="Foto: zwei geöffnete Hände, aus denen helles Licht und rosa Lichtpartikel aufsteigen"></div>

    <h1 class="title">
      <span class="title-line-one">QUELLKRAFT DER</span>
      <span class="title-line-two">LEITSÄTZE</span>
    </h1>
    <p class="subtitle">Gesundheit für Körper und Seele</p>
    <div class="ornament" role="img" aria-label="Geschwungenes Zierornament"></div>
    <p class="authors">von Renate Kolbeck &amp; Matthias Grauwald</p>

    <svg class="badge" viewBox="0 0 124 124" aria-label="Gratis-Download der Meditation „Der Fluss der Klärung, Stärkung und Erneuerung“">
      <defs>
        <path id="badge-ring" d="M62,62 m-48,0 a48,48 0 1,1 96,0 a48,48 0 1,1 -96,0"/>
      </defs>
      <circle cx="62" cy="62" r="60" fill="#f3e6f0"/>
      <circle cx="62" cy="62" r="57" fill="var(--badge)"/>
      <circle cx="62" cy="62" r="40" fill="#f6eef4"/>
      <circle cx="62" cy="62" r="37" fill="var(--badge)"/>
      <text font-size="8.6" fill="#ffffff" letter-spacing="0.3">
        <textPath href="#badge-ring" startOffset="2%">„DER FLUSS DER KLÄRUNG, STÄRKUNG UND ERNEUERUNG“</textPath>
      </text>
      <text x="62" y="52" text-anchor="middle" font-size="10" fill="#ffffff">GRATIS-</text>
      <text x="62" y="65" text-anchor="middle" font-size="10" fill="#ffffff">DOWNLOAD DER</text>
      <text x="62" y="78" text-anchor="middle" font-size="10" fill="#ffffff">MEDITATION</text>
    </svg>
  </main>
</body>
</html>
```